Dog Coat Drive for San Francisco Homeless Pets

- one page, full color, flyer to advertise a winter dog coat drive.- requesting use of an image of pit bull type or chihuahua type dog in a coat - 2 size versions - 8.5 inch by 11 inch to be printed and a square design to be posted on FB, Instagram and websites

Font styles to use
Serif
Sans Serif

Colors

Designer to choose colors to be used in the design.

```html
<!DOCTYPE html>
<html lang="en">
<head>
<meta charset="utf-8">
<title>Dog Coat Drive Flyer</title>
<link rel="stylesheet" href="https://fonts.googleapis.com/css2?family=Tinos:wght@400;700&display=swap">
<style>
  :root {
    --blue: #2f86cf;
    --blue-deep: #1f6fb8;
    --charcoal: #3a3b3f;
    --ink: #2b2b2b;
    --paper: #ffffff;
    --panel: #eef0f3;
    --rule: #c9ccd2;
    --backdrop: #b8a3b2;
    --orange: #d2591f;
  }
  * { box-sizing: border-box; margin: 0; padding: 0; }
  html, body { width: 1200px; height: 1037px; overflow: hidden; }
  body {
    background: var(--backdrop);
    font-family: "Tinos", "Times New Roman", serif;
    color: var(--ink);
    position: relative;
  }
  .flyer {
    position: absolute; left: 221px; top: 28px;
    width: 758px; height: 980px;
    background: var(--paper);
    overflow: hidden;
    box-shadow: 0 10px 30px rgba(60,30,50,.25);
  }
  .brand {
    position: absolute; left: 0; top: 0; width: 282px; height: 150px;
    display: flex; align-items: center; gap: 12px; padding: 0 22px;
  }
  .brand-mark { width: 34px; height: 34px; border-radius: 50%; background: var(--blue); flex: none; }
  .brand-name { font-size: 26px; line-height: 1.05; color: var(--charcoal); font-weight: 400; }
  .brand-sub { display: block; font-size: 9px; letter-spacing: .5px; margin-top: 6px; color: var(--charcoal); }
  .hero-photo {
    position: absolute; left: 282px; top: 0; width: 476px; height: 400px;
    background: radial-gradient(ellipse at 55% 60%, #b88a5e 0%, #a87b55 35%, #d9b991 70%, #ecd8bb 100%);
  }
  .title-block {
    position: absolute; left: 0; top: 150px; width: 270px; height: 250px;
    background: var(--blue);
    padding: 20px 0 0 34px;
  }
  .title-edge { position: absolute; left: 270px; top: 150px; width: 12px; height: 250px; background: var(--charcoal); }
  .title {
    color: #fff; font-weight: 700; font-size: 54px; line-height: 1.1;
    text-shadow: 0 2px 3px rgba(0,0,0,.25);
  }
  .title span { display: block; }
  .title .l2 { padding-left: 8px; }
  .title .l3 { padding-left: 22px; }

  .banner { position: absolute; left: 28px; top: 414px; width: 702px; height: 100px; }
  .banner svg { position: absolute; inset: 0; }
  .banner-left {
    position: absolute; left: 22px; top: 20px; font-size: 25px; line-height: 1.2; text-transform: uppercase;
  }
  .banner-left .light { color: #fff; }
  .banner-left .accent { color: var(--blue); }
  .banner-right {
    position: absolute; left: 405px; top: 22px; color: #fff; font-weight: 700;
    font-size: 22px; line-height: 1.25; text-transform: uppercase;
  }

  .appeal {
    position: absolute; left: 40px; right: 40px; top: 528px;
    text-align: center; font-size: 14px; line-height: 1.35; color: var(--ink);
  }
  .appeal strong { color: var(--blue); font-weight: 700; }

  .section-head { position: absolute; left: 0; right: 0; top: 580px; height: 40px; }
  .section-head::before {
    content: ""; position: absolute; left: 0; right: 0; top: 19px; height: 3px; background: var(--blue);
  }
  .section-pill {
    position: absolute; left: 160px; width: 438px; height: 40px; border-radius: 20px;
    background: var(--charcoal); color: #fff; font-size: 20px; text-transform: uppercase;
    display: flex; align-items: center; justify-content: center; letter-spacing: .3px;
  }

  .locations {
    position: absolute; left: 0; right: 0; top: 620px; height: 258px;
    background: linear-gradient(180deg, var(--panel), #f7f8fa);
  }
  .loc-row { position: absolute; display: flex; }
  .loc-row.first { left: 50px; top: 34px; width: 660px; }
  .loc-row.second { left: 95px; top: 150px; width: 620px; }
  .loc-rule { position: absolute; left: 80px; right: 40px; top: 128px; height: 1px; background: var(--rule); }
  .loc { padding: 0 16px; border-left: 1px solid var(--rule); }
  .loc:first-child { border-left: none; padding-left: 0; }
  .loc-row.first .loc { width: 220px; height: 80px; }
  .loc-row.second .loc { width: 300px; height: 80px; }
  .loc-name { color: var(--blue); font-weight: 700; font-size: 18px; margin-bottom: 6px; }
  .loc-line { display: flex; align-items: center; gap: 6px; font-size: 16px; line-height: 1.35; }
  .loc-line svg { width: 13px; height: 13px; flex: none; }

  .footer-rule { position: absolute; left: 0; right: 0; top: 878px; height: 3px; background: var(--ink); }
  .footer { position: absolute; left: 0; right: 0; top: 881px; bottom: 0; }
  .partner-main {
    position: absolute; left: 40px; top: 20px; width: 430px; text-align: center; color: var(--orange);
  }
  .partner-main .name { font-size: 28px; font-weight: 700; }
  .partner-main .details {
    display: flex; justify-content: space-between; font-size: 10px; letter-spacing: 1.5px;
    text-transform: uppercase; margin-top: 8px;
  }
  .partner-divider { position: absolute; left: 520px; top: 10px; width: 1px; height: 80px; background: var(--rule); }
  .partner-side { position: absolute; left: 540px; top: 12px; width: 200px; }
  .side-band {
    display: flex; align-items: center; gap: 10px; height: 30px; background: var(--blue-deep);
    color: #fff; font-size: 14px; font-weight: 700; letter-spacing: 1px; padding-left: 6px;
  }
  .side-band .square { width: 18px; height: 18px; background: #fff; }
  .badges { display: flex; gap: 14px; margin-top: 12px; padding-left: 12px; }
  .badge { width: 40px; height: 40px; border-radius: 50%; }
  .badge.dark { background: #2a2623; }
  .badge.light { background: #cfe3b4; }
</style>
</head>
<body>
  <main class="flyer">
    <header>
      <div class="brand">
        <span class="brand-mark"></span>
        <div class="brand-name">Harborview<br>Animal Care<span class="brand-sub">CITY OF HARBORVIEW</span></div>
      </div>
      <div class="hero-photo" role="img" aria-label="Photo of a tan pit bull type dog looking toward the camera against a soft warm background"></div>
      <div class="title-block">
        <h1 class="title"><span class="l1">Baby,</span><span class="l2">It’s Cold</span><span class="l3">Outside!</span></h1>
      </div>
      <div class="title-edge"></div>
    </header>

    <section class="banner">
      <svg width="702" height="100" viewBox="0 0 702 100" aria-hidden="true">
        <polygon points="340,12 702,12 702,90 340,90 370,51" fill="#2f86cf"/>
        <polygon points="0,0 345,0 385,50 345,100 0,100" fill="#3a3b3f"/>
      </svg>
      <div class="banner-left"><span class="light">Dog coat drive for</span><br><span class="accent">City Navigation Centers</span></div>
      <div class="banner-right">From December<br>through February</div>
    </section>

    <p class="appeal"><strong>Please donate</strong> new &amp; gently used dog coats, sweaters and jackets for Navigation Center dogs<br>whose owners are working to prevent and end their homelessness</p>

    <div class="section-head"><div class="section-pill">Coat drop partners and locations</div></div>

    <section class="locations">
      <svg width="0" height="0" style="position:absolute">
        <defs>
          <symbol id="pin" viewBox="0 0 16 16"><circle cx="8" cy="8" r="7" fill="none" stroke="#2f86cf" stroke-width="1.5"/><path d="M8 3.5a3 3 0 0 0-3 3c0 2.2 3 5.5 3 5.5s3-3.3 3-5.5a3 3 0 0 0-3-3z" fill="#2f86cf"/><circle cx="8" cy="6.5" r="1" fill="#fff"/></symbol>
          <symbol id="phone" viewBox="0 0 16 16"><circle cx="8" cy="8" r="7" fill="none" stroke="#2f86cf" stroke-width="1.5"/><path d="M5.5 4.2l1.4-.2.8 1.9-.9.8a5 5 0 0 0 2.5 2.5l.8-.9 1.9.8-.2 1.4c-3.4.4-6.7-2.9-6.3-6.3z" fill="#2f86cf"/></symbol>
        </defs>
      </svg>
      <div class="loc-row first">
        <div class="loc">
          <div class="loc-name">HV Animal Care</div>
          <div class="loc-line"><svg><use href="#pin"/></svg>820 Alder Street</div>
          <div class="loc-line"><svg><use href="#phone"/></svg>555-014-2200</div>
        </div>
        <div class="loc">
          <div class="loc-name">The Pet Parlor</div>
          <div class="loc-line"><svg><use href="#pin"/></svg>42 Larkspur Street</div>
          <div class="loc-line"><svg><use href="#phone"/></svg>555-013-4478</div>
        </div>
        <div class="loc">
          <div class="loc-name">Maple Hill Pet Co.</div>
          <div class="loc-line"><svg><use href="#pin"/></svg>309 Cedar Street</div>
          <div class="loc-line"><svg><use href="#phone"/></svg>555-016-9031</div>
        </div>
      </div>
      <div class="loc-rule"></div>
      <div class="loc-row second">
        <div class="loc">
          <div class="loc-name">Happy Tails Pet Services</div>
          <div class="loc-line"><svg><use href="#pin"/></svg>77 Seaview Drive, Bayport</div>
          <div class="loc-line"><svg><use href="#phone"/></svg>555-018-2764</div>
        </div>
        <div class="loc">
          <div class="loc-name">The Bowen Center</div>
          <div class="loc-line"><svg><use href="#pin"/></svg>510 Shoreline Avenue, Bayport</div>
          <div class="loc-line"><svg><use href="#phone"/></svg>555-019-6612</div>
        </div>
      </div>
    </section>

    <div class="footer-rule"></div>
    <footer class="footer">
      <div class="partner-main">
        <div class="name">The Pet Parlor</div>
        <div class="details"><span>42 Larkspur Street · Old Town Harborview</span><span>555-013-4478</span></div>
      </div>
      <div class="partner-divider"></div>
      <div class="partner-side">
        <div class="side-band"><span class="square"></span>THE BOWEN CENTER</div>
        <div class="badges"><span class="badge dark"></span><span class="badge light"></span></div>
      </div>
    </footer>
  </main>
</body>
</html>
```